Re-work our letterhead and create a matching cover page for our FB account

We need a new letterhead to reflect our new social media branding which contains the words Wealth Retirement & Aged Care underneath the name of the company Carrow Ledger Advisers Pty Ltd. We need this logo to be able to be used as a Cover page (in .png) for our Facebook account. Colours and format to be derived from files attached.

```html
<!DOCTYPE html>
<html lang="en">
<head>
<meta charset="utf-8">
<title>Carrow Ledger Advisers – Letterhead</title>
<link rel="stylesheet" href="https://fonts.googleapis.com/css2?family=Roboto:wght@400;500;700&family=Roboto+Condensed:wght@400;700&family=Great+Vibes&display=swap">
<style>
  :root {
    --gold: #c49a00;
    --gold-text: #c9a227;
    --ink: #111111;
    --grey: #5f6b70;
    --navy: #14264a;
    --paper: #ffffff;
    --backdrop: #ececec;
  }
  * { margin: 0; padding: 0; box-sizing: border-box; }
  html, body {
    width: 941px; height: 1200px; overflow: hidden;
    background: var(--backdrop);
  }
  .letterhead {
    position: absolute; left: 46px; top: 0;
    width: 848px; height: 1200px;
    background: var(--paper);
    font-family: "Roboto", sans-serif;
    color: var(--ink);
  }
  .brand { position: absolute; left: 92px; top: 80px; }
  .brand-name {
    font-family: "Roboto", sans-serif;
    font-weight: 700; font-size: 30px; line-height: 1;
    color: var(--ink); letter-spacing: -0.5px;
  }
  .brand-tagline {
    margin-top: 6px;
    font-family: "Roboto Condensed", sans-serif;
    font-size: 12px; color: var(--grey);
  }
  .contact-rule {
    position: absolute; left: 551px; top: 52px;
    width: 1.5px; height: 108px; background: var(--gold);
  }
  .contact {
    position: absolute; left: 565px; top: 62px;
    font-size: 11.5px; color: var(--gold-text); line-height: 1;
  }
  .contact-street { margin-bottom: 17px; }
  .contact-row { display: flex; align-items: center; height: 20px; }
  .contact-row svg { width: 15px; height: 15px; margin-right: 14px; fill: var(--gold-text); }
  .recipient { position: absolute; left: 103px; top: 231px; font-size: 16px; line-height: 20.6px; }
  .recipient-name { font-weight: 500; font-size: 19px; line-height: 22px; }
  .recipient-details { margin-top: 10px; }
  .date { position: absolute; right: 84px; top: 231px; text-align: right; font-size: 16px; line-height: 20.6px; }
  .date-label { font-size: 19px; line-height: 22px; }
  .letter-body {
    position: absolute; left: 103px; top: 405px; width: 661px;
    font-size: 16px; line-height: 20.6px;
  }
  .letter-body p { text-align: justify; hyphens: auto; margin-bottom: 20.6px; }
  .letter-body .greeting, .letter-body .closing { text-align: left; }
  .letter-body .closing { margin-bottom: 0; }
  .signature {
    position: absolute; left: 103px; top: 810px;
    font-family: "Great Vibes", cursive; font-size: 42px; color: var(--ink);
  }
  .signatory { position: absolute; left: 103px; top: 877px; font-family: "Roboto Condensed", sans-serif; }
  .signatory-name { font-weight: 700; font-size: 19px; color: var(--navy); line-height: 22px; }
  .signatory-role { font-size: 15px; line-height: 19px; }
  .footer-band { position: absolute; left: 0; bottom: 0; width: 100%; height: 38px; background: var(--gold); }
</style>
</head>
<body>
<main class="letterhead">
  <header>
    <div class="brand">
      <div class="brand-name">Carrow Ledger</div>
      <div class="brand-tagline">Wealth Retirement &amp; Aged Care</div>
    </div>
    <div class="contact-rule"></div>
    <address class="contact" style="font-style:normal">
      <div class="contact-street">42 Harlow Rd Brenton</div>
      <div class="contact-row">
        <svg viewBox="0 0 24 24" aria-hidden="true"><path d="M6.6 10.8a15.1 15.1 0 0 0 6.6 6.6l2.2-2.2a1 1 0 0 1 1-.25 11.4 11.4 0 0 0 3.6.57 1 1 0 0 1 1 1V20a1 1 0 0 1-1 1A17 17 0 0 1 3 4a1 1 0 0 1 1-1h3.5a1 1 0 0 1 1 1c0 1.25.2 2.45.57 3.57a1 1 0 0 1-.25 1z"/></svg>
        <span>(03) 9100 5821</span>
      </div>
      <div class="contact-row">
        <svg viewBox="0 0 24 24" aria-hidden="true" style="fill:none;stroke:var(--gold-text);stroke-width:1.6"><circle cx="12" cy="12" r="9.5"/><ellipse cx="12" cy="12" rx="4.5" ry="9.5"/><path d="M2.5 12h19M4 7h16M4 17h16"/></svg>
        <span>www.carrowledgeradvisers.com.au</span>
      </div>
      <div class="contact-row">
        <svg viewBox="0 0 24 24" aria-hidden="true"><path d="M2 5h20v2l-10 6L2 7z"/><path d="M2 9l10 6 10-6v10H2z"/></svg>
        <span>PO Box 318 Kelmore Vic 3499</span>
      </div>
    </address>
  </header>

  <section class="recipient">
    <div class="recipient-name">Name</div>
    <div>Owner</div>
    <div class="recipient-details">
      000-000-0000<br>some @some.com<br>Some street, Some city<br>Some country
    </div>
  </section>

  <section class="date">
    <div class="date-label">Date</div>
    <div>31 December 2024</div>
  </section>

  <article class="letter-body" lang="la">
    <p class="greeting" lang="en">Dear Mr. Name</p>
    <p>Lorem ipsum dolor sit amet, consectetuer adipiscing elit, sed diam nonummy nibh euismod tincidunt ut laoreet dolore magna aliquam erat volutpat. Ut wisi enim ad minim veniam, quis nostrud exerci tation ullamcorper suscipit lobortis nisl ut aliquip ex ea commodo consequat. Duis autem vel eum iriure dolor in hendrerit in vulputate velit esse molestie.</p>
    <p>Lorem ipsum dolor sit amet, cons ectetuer adipiscing elit, sed diam nonummy nibh euismod tincidunt ut laoreet dolore magna aliquam erat volutpat. Ut wisi enim ad minim veniam, quis nostrud exerci tation ullamcorper suscipit lobortis nisl ut aliquip ex ea commodo consequat.</p>
    <p>Lorem ipsum dolor sit amet, consectetuer adipiscing elit, sed diam nonummy nibh euismod tincidunt ut laoreet dolore magna aliquam erat volutpat. Ut wisi enim ad minim veniam, quis nostrud exerci tation ullamcorper suscipit lobortis nisl ut aliquip ex ea commodo consequat.</p>
    <p class="closing" lang="en">Thank you.</p>
  </article>

  <div class="signature">Signature</div>
  <div class="signatory">
    <div class="signatory-name">Name</div>
    <div class="signatory-role">Owner</div>
  </div>

  <footer class="footer-band"></footer>
</main>
</body>
</html>
```